Holistic Therapy (aromatherapy, massage, reflexology, life coaching, soul healing, aura reading)

I work for myself as a holistic therapist doing: aromatherapy massage, massage, reflexology, abdominal-sacral massage, life coaching, soul healing, aura readings. I want a business card that doesn't focus on any one of these( so not just feet or a massage couch,but rather a card that creates the feeling of wholeness, healing, health and which can encompass all my therapies - e.g. green or purple are colours I like (especially green, or maybe green on back and purple on front). It's going to be called Rosa Elwin Therapies. I don't want to list all my therapies on the card in case I add others later.). At some point I will create a website but in this instance I just want to get some cards printed to get 'out there' while I design my website.
Updates

Hi, thanks for all your designs. Can you find a way to include the therapies that I offer within the card, either on the front or back…the therapies I offer are: aromatherapy massage, reflexology, swedish body massage, abdominal-sacral massage, nutrition, soul healing, aura readings. (Maybe have them with a bullet point before each?) I am not sure whether they should be on the front of the card or the back or whether having them would spoil the card but it occurred to me that just having rosa elwin therapies doesn't tell people what therapies I offer, hence the new idea to list them somehow…)

Target Market(s)

Mainly women (middle class probably with disposable incomes).

Industry/Entity Type

Massage

Contact Information for Business Card

Rosa Elwin Therapies, Tel: 07942 586113, email: vitalbloom@mailvane.com, (on back of card I want: Rosalind Elwin BScHons, OKQRB, GPCL.)

Requirements
Nice to have
• A logo for Rosa Elwin Therapies would be good.

```html
<!DOCTYPE html>
<html lang="en">
<head>
<meta charset="utf-8">
<title>Rosa Elwin Therapies – Business Card</title>
<link rel="stylesheet" href="https://fonts.googleapis.com/css2?family=Mulish:wght@400;700&display=swap">
<style>
  :root {
    --canvas-bg: #ececec;
    --green-mid: #d7f7b8;
    --green-deep: #b6ef86;
    --mark-fill: #c27aa8;
    --brand-pink: #b5508a;
    --ink: #2b2b2b;
    --card-shadow: rgba(0, 0, 0, 0.28);
  }
  * { margin: 0; padding: 0; box-sizing: border-box; }
  html, body {
    width: 976px;
    height: 1200px;
    overflow: hidden;
    background: var(--canvas-bg);
    font-family: "Mulish", "Century Gothic", sans-serif;
  }
  .card {
    position: absolute;
    border-radius: 24px;
    overflow: hidden;
    box-shadow: 6px 8px 10px var(--card-shadow);
  }
  .card-front { left: 89px; top: 89px; width: 773px; height: 456px; }
  .card-back {
    left: 87px; top: 628px; width: 772px; height: 455px;
    background: radial-gradient(ellipse 62% 70% at 58% 45%, #ffffff 0%, var(--green-mid) 60%, var(--green-deep) 100%);
  }
  .card-front svg { position: absolute; inset: 0; }
  .brand-mark {
    position: absolute;
    border-radius: 50%;
    background: var(--mark-fill);
  }
  .card-front .brand-mark { left: 115px; top: 85px; width: 230px; height: 230px; }
  .card-back .brand-mark { left: 40px; top: 60px; width: 110px; height: 110px; }
  .brand-name {
    position: absolute;
    color: var(--brand-pink);
    font-weight: 400;
    line-height: 1.1;
    letter-spacing: 0.5px;
  }
  .card-front .brand-name { left: 342px; top: 240px; font-size: 46px; }
  .card-back .brand-name { left: 156px; top: 146px; font-size: 24px; }
  .contact {
    position: absolute;
    right: 112px;
    text-align: right;
    color: var(--ink);
    white-space: nowrap;
  }
  .contact-name { top: 246px; font-size: 22px; font-weight: 700; }
  .contact-phone { top: 300px; font-size: 22px; font-weight: 700; display: flex; align-items: center; gap: 10px; }
  .contact-email { top: 346px; font-size: 21px; font-weight: 400; display: flex; align-items: center; gap: 10px; }
  .icon { width: 26px; height: 26px; }
</style>
</head>
<body>
  <section class="card card-front" aria-label="Card front">
    <svg viewBox="0 0 773 456" width="773" height="456" aria-hidden="true">
      <defs>
        <radialGradient id="front-green" cx="0.2" cy="0.4" r="0.7">
          <stop offset="0" stop-color="#f4fde9"/>
          <stop offset="1" stop-color="#b9f08a"/>
        </radialGradient>
        <radialGradient id="front-purple" cx="0.62" cy="0.42" r="0.55">
          <stop offset="0" stop-color="#ffffff"/>
          <stop offset="0.55" stop-color="#e6c5df"/>
          <stop offset="1" stop-color="#c48ec0"/>
        </radialGradient>
      </defs>
      <rect class="front-green-field" width="773" height="456" fill="url(#front-green)"/>
      <path class="front-purple-field" d="M467 0 L773 0 L773 456 L227 456 C250 420 262 380 300 330 C360 260 445 190 467 0 Z" fill="url(#front-purple)"/>
      <path class="front-divider" d="M467 0 C445 190 360 260 300 330 C262 380 250 420 227 456" fill="none" stroke="#eaf9dc" stroke-width="4"/>
    </svg>
    <div class="brand-mark" role="img" aria-label="Brand mark position"></div>
    <div class="brand-name">Rosa Elwin<br>Therapies</div>
  </section>

  <section class="card card-back" aria-label="Card back">
    <div class="brand-mark" role="img" aria-label="Brand mark position"></div>
    <div class="brand-name">Rosa Elwin<br>Therapies</div>
    <div class="contact contact-name">Rosalind Elwin BScHons, OKQRB, GPCL.</div>
    <div class="contact contact-phone">
      <svg class="icon" viewBox="0 0 26 26" aria-hidden="true">
        <circle cx="13" cy="13" r="11.5" fill="none" stroke="#2b2b2b" stroke-width="1.4"/>
        <path d="M9 7.5 C7.5 9 8 12 10.5 15 C13 18 16 19 17.8 17.6 L16.2 15.4 L14.6 16.2 C13.4 15.5 11.6 13.6 11 12.2 L12 10.8 Z" fill="#2b2b2b"/>
      </svg>
      <span>07942 586113</span>
    </div>
    <div class="contact contact-email">
      <svg class="icon" viewBox="0 0 26 26" aria-hidden="true">
        <rect x="2" y="6" width="22" height="14" fill="none" stroke="#2b2b2b" stroke-width="1.6"/>
        <path d="M2 6 L13 14.5 L24 6 M2 20 L10 12.5 M24 20 L16 12.5" fill="none" stroke="#2b2b2b" stroke-width="1.6"/>
      </svg>
      <span>vitalbloom@mailvane.com</span>
    </div>
  </section>
</body>
</html>
```